Business cards & stationary
QVM247: Tuition Debt Relief
Use same font as used in my logo
Use logo font in logo, but easier to read font for rest of card
Simple
Gavin Morrow
President & CEO
2918 Fernhollow Dr
Blacklick, OH 43871
1-855-7-QVM-247
gmorrow@QVM247.example
www.QVM247.example
Please see logo project.
TBD. For now, please have an image take up the back...part or all of logo. Or just the top part "QVM247.example"
logo in AI format
logo color info

```html
<!DOCTYPE html>
<html lang="en">
<head>
<meta charset="utf-8">
<title>QVM247 Business Cards</title>
<link href="https://fonts.googleapis.com/css2?family=Oswald:wght@700&family=Open+Sans:wght@400;600;700&display=swap" rel="stylesheet">
<style>
  :root {
    --stage: #1b2127;
    --card: #ffffff;
    --green: #1f8a3c;
    --green-dark: #17692d;
    --ink: #2b2b2b;
    --muted: #6d6d6d;
  }
  * { box-sizing: border-box; margin: 0; padding: 0; }
  html, body { width: 1200px; height: 874px; overflow: hidden; }
  body {
    background: var(--stage);
    font-family: "Open Sans", sans-serif;
    display: flex;
    align-items: center;
    justify-content: center;
    gap: 40px;
  }
  .card {
    position: relative;
    width: 540px;
    height: 309px;
    background: var(--card);
    border-radius: 14px;
    overflow: hidden;
  }
  .brand {
    position: absolute;
    display: flex;
    align-items: center;
    gap: 10px;
    font-family: "Oswald", sans-serif;
    font-weight: 700;
    color: var(--green);
    line-height: 1;
    white-space: nowrap;
  }
  .brand-mark { width: 16px; height: 16px; background: var(--green); }
  .front .brand { left: 40px; top: 108px; font-size: 64px; }
  .back .brand { left: 50%; top: 50%; transform: translate(-50%, -58%); font-size: 78px; }
  .back .brand-mark { width: 20px; height: 20px; }

  .person { position: absolute; right: 30px; top: 26px; text-align: right; }
  .person-name { font-weight: 700; font-size: 15px; color: var(--ink); }
  .person-title { font-size: 10px; color: var(--muted); margin-top: 1px; }

  .contact { position: absolute; right: 30px; top: 96px; list-style: none; text-align: right; }
  .contact li {
    display: flex; justify-content: flex-end; align-items: center; gap: 7px;
    font-size: 10.5px; color: var(--ink); line-height: 18px; white-space: nowrap;
  }
  .contact svg { width: 9px; height: 9px; fill: var(--green); flex: none; }

  .rule { position: absolute; left: 0; bottom: 30px; height: 14px; }
  .web {
    position: absolute; right: 30px; bottom: 25px;
    font-weight: 700; font-size: 12px; letter-spacing: 1px; color: var(--ink);
  }
</style>
</head>
<body>

<section class="card front">
  <div class="brand"><span class="brand-mark"></span>QVM247</div>

  <div class="person">
    <p class="person-name">Gavin Morrow</p>
    <p class="person-title">President &amp; CEO</p>
  </div>

  <ul class="contact">
    <li>2918 Fernhollow Dr<svg viewBox="0 0 10 10"><path d="M5 0a3.5 3.5 0 0 0-3.5 3.5C1.5 6 5 10 5 10s3.5-4 3.5-6.5A3.5 3.5 0 0 0 5 0z"/></svg></li>
    <li>Cedarbrook, OH 43871<svg viewBox="0 0 10 10"><rect width="10" height="10" rx="1"/></svg></li>
    <li>1-855-7-QVM-247<svg viewBox="0 0 10 10"><path d="M2 0l2 2.5-1 1.5a6 6 0 0 0 3 3l1.5-1L10 8 8.5 10C4 10 0 6 0 1.5z"/></svg></li>
    <li>614-555-0192<svg viewBox="0 0 10 10"><rect y="3" width="10" height="7" rx="1"/><rect x="2" width="6" height="4"/></svg></li>
    <li>gmorrow@QVM247.example<svg viewBox="0 0 10 10"><circle cx="5" cy="5" r="5"/></svg></li>
  </ul>

  <svg class="rule" width="320" height="14" viewBox="0 0 320 14">
    <line x1="0" y1="7" x2="312" y2="7" stroke="var(--green)" stroke-width="1.5"/>
    <circle cx="312" cy="7" r="4" fill="var(--green-dark)"/>
  </svg>
  <p class="web">www.QVM247.example</p>
</section>

<section class="card back">
  <div class="brand"><span class="brand-mark"></span>QVM247</div>

  <svg class="rule" width="320" height="14" viewBox="0 0 320 14">
    <line x1="0" y1="7" x2="312" y2="7" stroke="var(--green)" stroke-width="1.5"/>
    <circle cx="312" cy="7" r="4" fill="var(--green-dark)"/>
  </svg>
  <p class="web">www.QVM247.example</p>
</section>

</body>
</html>
```